a business advisory consulting website

I need a website 3-5 pages to sell my professional services in IT and Project management Consulting. My company name is Northwell Strategy Consulting. I want it to be device friendly and easy to navigate for the busy executive however intriguing enough.
I have attached some info I drafted on About the company and personal Bio. Also there is a website that I really like that I have attached the initial site pdf and websites that I like are here: https://quillmarshcapital.example, https://tandermoviews.example, https://www.felkinlearningconsulting.example as examples. Thanks
Updates

Hi Designers, I have uploaded the logo in 3D .png format, to assist in the web design.

Target Market(s)

B2B, governments, IT companies, Project Management companies and Consulting firms, small medium enterprises to large corporate enterprises.

Industry/Entity Type

It Professional

Coding

Coded - Design and coding required

Number of Pages Required

5+ page

Font styles to use
Sans Serif

Requirements
Must have
• Home, About company, the team, what we do and contact us
Nice to have
• Blog
Should not have
• pop ups, flash

```html
<!DOCTYPE html>
<html lang="en">
<head>
<meta charset="utf-8">
<title>Northwell Strategy Consulting</title>
<link href="https://fonts.googleapis.com/css2?family=Lato:wght@400;700&family=Roboto:wght@400;500;700&display=swap" rel="stylesheet">
<style>
:root{
  --navy:#262a4b;
  --ink:#1c1f5e;
  --red:#f23e3e;
  --red-deep:#e32b35;
  --pink:#fddcdd;
  --pink-soft:#fbe3e4;
  --page:#f6f7f9;
  --cream:#fdf6f5;
  --text:#3d4050;
  --white:#ffffff;
}
*{margin:0;padding:0;box-sizing:border-box}
html,body{width:1200px;height:3164px;overflow:hidden}
body{position:relative;background:var(--page);font-family:'Lato',sans-serif;color:var(--text)}
.abs{position:absolute}
.topbar{left:0;top:0;width:1200px;height:30px;background:var(--navy)}
.topbar .phone{left:163px;top:8px;font-size:11px;color:var(--white);display:flex;align-items:center;gap:8px}
.topbar .cta{left:906px;top:6px;width:144px;height:19px;background:var(--red-deep);border:1px solid #fff5;color:#fff;font-size:9.5px;font-weight:700;font-family:'Roboto',sans-serif;display:flex;align-items:center;justify-content:center}
.nav{left:0;top:30px;width:1200px;height:74px;background:var(--cream)}
.brand{left:150px;top:22px;display:flex;align-items:center;gap:8px;font-family:'Roboto',sans-serif;font-weight:700;font-size:18px;color:var(--ink);letter-spacing:.5px}
.brand .mark{width:22px;height:22px;background:var(--red)}
.menu{right:149px;top:29px;display:flex;gap:33px;font-family:'Roboto',sans-serif;font-weight:500;font-size:15px;color:#2a3490}
.hero{left:0;top:104px;width:1200px;height:543px;background:linear-gradient(90deg,#f4f4f4,#fafafa 55%,#fff)}
.hero .redblock{left:806px;top:0;width:394px;height:543px;background:var(--red)}
.hero .portrait{left:640px;top:20px;width:373px;height:523px;background:linear-gradient(180deg,#8a6a55 0%,#2b2b30 35%,#111 100%);border-radius:140px 140px 0 0}
.hero h1{left:150px;top:162px;width:520px;font-family:'Roboto',sans-serif;font-weight:700;font-size:48px;line-height:53px;color:#2b2f55}
.hero p{left:152px;top:272px;width:430px;font-size:13px;line-height:15px;color:#8a8a90}
.btn{background:var(--red);color:#fff;font-family:'Lato',sans-serif;font-weight:700;display:flex;align-items:center;justify-content:center;border-radius:2px}
.hero .btn{left:151px;top:336px;width:150px;height:33px;font-size:13.5px}
.section-title{font-family:'Roboto',sans-serif;font-weight:700;font-size:31px;color:var(--ink);display:inline-block}
.section-title::after{content:"";position:absolute;left:8px;bottom:-2px;height:13px;background:#f6b9bc;width:calc(100% - 8px);z-index:-1}
.card{width:275px;height:130px;background:var(--white);box-shadow:0 2px 6px #0000000d;overflow:hidden;display:flex;align-items:center;justify-content:center;text-align:center;font-size:23px;line-height:27px;color:var(--ink)}
.card .plus{position:absolute;right:0;top:0;width:54px;height:54px;background:var(--pink);border-radius:0 0 0 54px}
.card .plus svg{position:absolute;left:17px;top:10px}
.why{left:150px;top:1306px;width:850px;font-size:19.5px;line-height:31.5px;color:#3a3d5e}
.band{left:0;top:1572px;width:1200px;height:259px;background:var(--navy);color:#fff;text-align:center}
.band h2{position:absolute;left:0;width:1200px;top:34px;font-size:27px;font-weight:700;font-family:'Lato',sans-serif}
.band p{position:absolute;left:225px;width:750px;top:76px;font-size:15px;line-height:28.5px}
.band .btn{left:521px;top:180px;width:163px;height:38px;font-size:13px}
.team-band{left:0;top:2027px;width:936px;height:343px;background:var(--pink)}
.team-photo{left:810px;top:2045px;width:209px;height:325px;background:linear-gradient(180deg,#6b4a3a 0%,#4a1f1b 40%,#3a1512 100%);border-radius:100px 100px 0 0}
.member-name{left:211px;top:2065px;font-family:'Roboto',sans-serif;font-weight:700;font-size:27px;color:#2b2f55}
.member-role{left:211px;top:2101px;display:flex;align-items:center;gap:3px;font-family:'Roboto',sans-serif;font-weight:700;font-size:15px;color:#2b2f55}
.member-role span{display:block;width:92px;height:2px;background:var(--red)}
.member-bio{left:212px;top:2138px;width:550px;font-size:14px;line-height:24px;color:#5a5a66}
.viewall{left:978px;top:2385px;font-family:'Roboto',sans-serif;font-weight:500;font-size:15.5px;color:var(--red-deep)}
.post{width:272px;height:174px;border-radius:6px;padding:18px 28px;font-size:14px}
.post .date{font-size:12px;margin-bottom:23px}
.post .title{line-height:25.5px;height:76px}
.post .by{position:absolute;left:28px;bottom:18px;font-size:10.5px}
.post.feature{background:linear-gradient(135deg,#4a5268,#2e3346 60%,#3d4459);color:#fff;box-shadow:0 3px 8px #0003}
.post.outline{background:#fff;border:1.5px solid #f3a4a7;color:var(--red-deep)}
.footer{left:0;top:2833px;width:1200px;height:331px;background:var(--navy);color:#fff}
.footer h4{position:absolute;top:44px;font-family:'Roboto',sans-serif;font-weight:500;font-size:13px}
.footer ul{position:absolute;top:95px;list-style:none;font-family:'Roboto',sans-serif;font-size:12px;line-height:30px}
.footer address{position:absolute;left:562px;top:94px;font-style:normal;font-family:'Roboto',sans-serif;font-size:12px;line-height:19px}
.social{position:absolute;top:210px;left:558px;display:flex;gap:16px}
.social span{width:23px;height:23px;border-radius:50%;background:#fff}
.field{position:absolute;left:782px;width:229px;background:#f4f4f4;border:1px solid #ccc;border-radius:2px;font-size:9px;color:#999;padding:7px 12px;font-family:'Roboto',sans-serif}
.submit{position:absolute;left:782px;top:239px;width:74px;height:26px;background:var(--red-deep);border:1px solid #fff7;border-radius:3px;font-size:11px;display:flex;align-items:center;justify-content:center;font-family:'Roboto',sans-serif}
.footer .rule{position:absolute;left:188px;top:292px;width:824px;height:1px;background:#ffffff30}
.footer .legal{position:absolute;top:303px;font-size:10px;font-family:'Roboto',sans-serif}
</style>
</head>
<body>

<header>
  <div class="abs topbar">
    <div class="abs phone">
      <svg width="12" height="12" viewBox="0 0 24 24"><path fill="#fff" d="M6.6 10.8a15 15 0 0 0 6.6 6.6l2.2-2.2c.3-.3.7-.4 1-.2 1.1.4 2.3.6 3.6.6.6 0 1 .4 1 1V20c0 .6-.4 1-1 1A17 17 0 0 1 3 4c0-.6.4-1 1-1h3.5c.6 0 1 .4 1 1 0 1.3.2 2.5.6 3.6.1.3 0 .7-.2 1z"/></svg>
      +44 20 7946 0321
    </div>
    <div class="abs cta">GET FREE CONSULTATION</div>
  </div>
  <nav class="abs nav">
    <div class="abs brand"><span class="mark"></span>NORTHWELL STRATEGY</div>
    <div class="abs menu"><span>HOME</span><span>OUR APPROACH</span><span>WHAT WE DO</span><span>TEAM</span><span>BLOGS</span><span>CONTACT</span></div>
  </nav>
</header>

<section class="abs hero">
  <div class="abs redblock"></div>
  <div class="abs portrait" role="img" aria-label="Portrait of a bearded consultant in a dark suit with arms crossed"></div>
  <h1 class="abs">We Help Building Up Your Business</h1>
  <p class="abs">We are a specialist operational excellence firm, delivering consulting and advisory services in six core capabilities, across all industries and all business lines to improve</p>
  <div class="abs btn">GET IN TOUCH</div>
</section>

<section>
  <div class="abs" style="left:152px;top:748px"><h2 class="section-title" style="position:relative;z-index:1">Our Services</h2></div>
  <div class="abs card" style="left:151px;top:840px"><span class="plus"><svg width="22" height="22"><path d="M11 0v22M0 11h22" stroke="#f23e3e" stroke-width="1.6"/></svg></span>Market Entry</div>
  <div class="abs card" style="left:463px;top:840px"><span class="plus"><svg width="22" height="22"><path d="M11 0v22M0 11h22" stroke="#f23e3e" stroke-width="1.6"/></svg></span>Strategy Analytics</div>
  <div class="abs card" style="left:775px;top:840px"><span class="plus"><svg width="22" height="22"><path d="M11 0v22M0 11h22" stroke="#f23e3e" stroke-width="1.6"/></svg></span>Business-Process<br>Optimization</div>
  <div class="abs card" style="left:151px;top:1000px"><span class="plus"><svg width="22" height="22"><path d="M11 0v22M0 11h22" stroke="#f23e3e" stroke-width="1.6"/></svg></span>Advise for Early<br>Stage Startups</div>
  <div class="abs card" style="left:463px;top:1000px"><span class="plus"><svg width="22" height="22"><path d="M11 0v22M0 11h22" stroke="#f23e3e" stroke-width="1.6"/></svg></span>Accounting</div>
  <div class="abs card" style="left:775px;top:1000px"><span class="plus"><svg width="22" height="22"><path d="M11 0v22M0 11h22" stroke="#f23e3e" stroke-width="1.6"/></svg></span>Insurance</div>
</section>

<section>
  <div class="abs" style="left:150px;top:1228px"><h2 class="section-title" style="position:relative;z-index:1">Why we Exist</h2></div>
  <p class="abs why">Our aim at Northwell Strategy is to be a leading strategy and financial advisory firm across the continent solving complex management problems for small and medium sized enterprises across a wide range of industries. We help you scale your business operations to become highly profitable. We offer your organization cutting-edge expertise leveraging on first-class, strategic and financial insights that help you simplify and structure your processes to become a lean efficient enterprise.</p>
</section>

<section class="abs band">
  <h2>WHY YOU SHOULD CONTACT TODAY?</h2>
  <p>We’re known for our pragmatism, in depth analysis, strategic insight and nurturing long-term client self-sufficiency. We approach business consulting differently, with a Genuine Client Partnership model that builds client capability and rightsized solutions for the client.</p>
  <div class="abs btn">CONTACT US</div>
</section>

<section>
  <div class="abs" style="left:151px;top:1942px"><h2 class="section-title" style="position:relative;z-index:1">Meet our Team</h2></div>
  <div class="abs team-band"></div>
  <div class="abs team-photo" role="img" aria-label="Photo of a smiling team member in glasses and a maroon shirt"></div>
  <div class="abs member-name">Daniel Okafor</div>
  <div class="abs member-role"><span></span>IT Professional</div>
  <p class="abs member-bio">Daniel Okafor is an IT professional with more than 20 years of experience turning business initiatives into technology solutions. His expertise has been identifying deficiencies and developing or facilitating the best solutions for an outcome that is satisfactory to all stakeholders involved.<br>Daniel improves business processes as older organizations restructure or migrate to newer technologies. He bridges the gap between the actual people in these organizations transitioning and the new technologies they seek which is a value add to any organization's success.</p>
  <div class="abs viewall">View All...</div>
</section>

<section>
  <div class="abs" style="left:151px;top:2484px"><h2 class="section-title" style="position:relative;z-index:1">Blog</h2></div>
  <article class="abs post feature" style="left:150px;top:2573px" role="img" aria-label="Blog card over a photo of hands typing on a laptop">
    <div class="date">23 march 2020</div>
    <div class="title">Consulting Fees Study 2019 (And How To Raise Your Rates)</div>
    <div class="by">By &nbsp;Aaron Whitfield - 20 Comments</div>
  </article>
  <article class="abs post outline" style="left:462px;top:2573px">
    <div class="date">17 May 2020</div>
    <div class="title">Don’t Focus on Leads For Your Consulting Business (Until You’ve Done This)</div>
    <div class="by">By &nbsp;Aaron Whitfield - 25 Comments</div>
  </article>
  <article class="abs post outline" style="left:776px;top:2573px">
    <div class="date">20 December 2020</div>
    <div class="title">Health &amp; Wellness For Consultants Study (2020)</div>
    <div class="by">By &nbsp;Aaron Whitfield - 63 Comments</div>
  </article>
</section>

<footer class="abs footer">
  <h4 style="left:188px">QUICK LINKS</h4>
  <ul style="left:188px"><li>Home</li><li>About The Ceo</li><li>Services</li><li>Testimonials</li><li>Contact</li></ul>
  <h4 style="left:377px">ABOUT</h4>
  <ul style="left:377px"><li>Pricing</li><li>Customers</li><li>Company</li><li>Blog</li><li>Careers</li></ul>
  <h4 style="left:562px">CONTACT US</h4>
  <address>Northwell Strategy Consulting<br>1820 Larchmere Avenue,<br>Brookfield 60513</address>
  <div class="social"><span></span><span></span><span></span><span></span></div>
  <h4 style="left:782px">QUICK INQUIRY</h4>
  <div class="field" style="top:83px;height:28px">Email</div>
  <div class="field" style="top:119px;height:28px">Subject</div>
  <div class="field" style="top:154px;height:61px">Enter your message</div>
  <div class="submit">Submit</div>
  <div class="rule"></div>
  <div class="legal" style="left:189px">Copyright © 2020 &nbsp;&nbsp; All Rights Reserved</div>
  <div class="legal" style="left:857px">Terms of Use &nbsp;&nbsp;| &nbsp;&nbsp;Privacy Policy</div>
</footer>

</body>
</html>
```